Design of Labels for Harrowmere Dock Spirit bottle

Design bottle labels for Harrowmere Dock Spirit. There are three labels to design; a front, a back and a tamper band to be placed over the cork. The labels should be deigned to fit the bottle specified in the link below.
The Gin is an excellent high end premium brand Navy strength Gin 57% Vol. The bottle should evoke excellence and a romance of period of pride in the British Navy. Gin was drunk by officers in the Navy so a representation of the Officer Class should be made possibly through gold braid of a senior officer's sleeve, cap or lapel. The white ensign should also be prominent. Suggested colour themes are navy blues, grey, and white....although others schemes may be suitable. Pellick's Quay Brandy is a good example of the sort of thing we are looking for, although the design must not be so similar that it encroaches on Pellick's trade mark or copyrights. The period theme is 1900 to 1940
Bottle link: https://www.vessel-crate-supply.co.uk/Glass-bottles/350ml-flint-glass-bottle-Marlo.html
Target Market(s)
Gin Drinkers
Look and feel

```html
<!DOCTYPE html>
<html lang="en">
<head>
<meta charset="utf-8">
<title>Harrowmere Dock Spirit – Front Label</title>
<link href="https://fonts.googleapis.com/css2?family=Montserrat:wght@300;400;700;800&family=Pinyon+Script&display=swap" rel="stylesheet">
<style>
  :root {
    --backdrop: #2b2d30;
    --navy-deep: #0c1f4a;
    --navy-mid: #1f3f86;
    --navy-light: #5f79b4;
    --navy-ink: #0a1a3f;
    --braid-gold: #d9ad3c;
    --paper-white: #e9ecf2;
    --mist: #c9d0de;
  }
  html, body {
    margin: 0;
    padding: 0;
    width: 1200px;
    height: 1000px;
    overflow: hidden;
    background: var(--backdrop);
  }
  .canvas {
    position: relative;
    width: 1200px;
    height: 1000px;
    background: var(--backdrop);
  }
  .front-label {
    position: absolute;
    left: 340px;
    top: 50px;
    width: 520px;
    height: 900px;
  }
  .label-shape {
    position: absolute;
    inset: 0;
    width: 520px;
    height: 900px;
  }
  .label-content {
    position: absolute;
    inset: 0;
    text-align: center;
    font-family: "Montserrat", sans-serif;
    color: var(--paper-white);
  }
  .crown-mark {
    position: absolute;
    left: 230px;
    top: 28px;
    width: 60px;
    height: 52px;
    border-radius: 6px;
    background: linear-gradient(180deg, #f4f6fa, var(--mist));
  }
  .ensign-flag {
    position: absolute;
    left: 174px;
    top: 145px;
    width: 172px;
    height: 77px;
    background: linear-gradient(135deg, #eef0f5 0%, #c9cfdc 60%, #b9c0d2 100%);
  }
  .brand-name {
    position: absolute;
    left: 0;
    right: 0;
    top: 252px;
    margin: 0;
    font-weight: 800;
    color: var(--paper-white);
    line-height: 1;
    letter-spacing: 1px;
  }
  .brand-name .line-one {
    display: block;
    font-size: 54px;
  }
  .brand-name .line-two {
    display: block;
    font-size: 78px;
    margin-top: 8px;
  }
  .ship-illustration {
    position: absolute;
    left: 131px;
    top: 418px;
    width: 258px;
    height: 112px;
    border-radius: 4px;
    background: radial-gradient(ellipse at 50% 60%, #0e2150 0%, rgba(31,63,134,0.6) 60%, rgba(31,63,134,0) 100%);
  }
  .tagline {
    position: absolute;
    left: 0;
    right: 0;
    top: 540px;
    margin: 0;
    font-family: "Pinyon Script", cursive;
    line-height: 1;
  }
  .tagline .quality {
    display: block;
    font-size: 38px;
    color: var(--paper-white);
  }
  .tagline .strength {
    display: block;
    font-size: 30px;
    color: var(--navy-ink);
    margin-top: 14px;
  }
  .product-type {
    position: absolute;
    left: 0;
    right: 0;
    top: 660px;
    margin: 0;
    font-weight: 300;
    font-size: 56px;
    letter-spacing: 4px;
    color: var(--mist);
  }
  .strength-abv {
    position: absolute;
    left: 0;
    right: 0;
    top: 742px;
    margin: 0;
    font-weight: 400;
    font-size: 22px;
    color: var(--mist);
  }
  .volume {
    position: absolute;
    left: 22px;
    top: 784px;
    margin: 0;
    font-size: 14px;
    color: var(--mist);
  }
  .anchor-icon {
    position: absolute;
    left: 238px;
    top: 826px;
    width: 44px;
    height: 48px;
  }
</style>
</head>
<body>
<main class="canvas">
  <section class="front-label">
    <svg class="label-shape" viewBox="0 0 300 520" preserveAspectRatio="none" aria-hidden="true">
      <defs>
        <radialGradient id="labelNavy" cx="50%" cy="48%" r="65%">
          <stop offset="0%" stop-color="#5f79b4"/>
          <stop offset="45%" stop-color="#1f3f86"/>
          <stop offset="100%" stop-color="#0c1f4a"/>
        </radialGradient>
      </defs>
      <path d="M0,48 Q0,34 14,30 L96,30 Q112,30 120,16 Q150,-6 180,16 Q188,30 204,30 L286,30 Q300,34 300,48 L300,450 L150,520 L0,450 Z"
            fill="url(#labelNavy)"/>
      <path d="M8,52 Q8,40 20,38 L98,38 Q116,38 125,23 Q150,4 175,23 Q184,38 202,38 L280,38 Q292,40 292,52 L292,445 L150,511 L8,445 Z"
            fill="none" stroke="#d9ad3c" stroke-width="2.2"/>
    </svg>

    <div class="label-content">
      <div class="crown-mark" role="img" aria-label="Small royal crown emblem"></div>
      <div class="ensign-flag" role="img" aria-label="White ensign flag, white field with red cross and union canton"></div>

      <h1 class="brand-name">
        <span class="line-one">HARROWMERE</span>
        <span class="line-two">DOCK</span>
      </h1>

      <div class="ship-illustration" role="img" aria-label="Silhouette of a three-masted sailing warship"></div>

      <p class="tagline">
        <span class="quality">Premium Quality</span>
        <span class="strength">Navy Strength</span>
      </p>

      <p class="product-type">SPIRIT</p>
      <p class="strength-abv">57%vol</p>
      <p class="volume">e35ml</p>

      <svg class="anchor-icon" viewBox="0 0 44 48" aria-label="Anchor" role="img">
        <g fill="none" stroke="#e9ecf2" stroke-width="3" stroke-linecap="round">
          <circle cx="22" cy="6" r="4"/>
          <line x1="22" y1="10" x2="22" y2="44"/>
          <line x1="13" y1="17" x2="31" y2="17"/>
          <path d="M5,30 Q8,44 22,44 Q36,44 39,30"/>
        </g>
        <path d="M2,32 L8,27 L9,34 Z M42,32 L36,27 L35,34 Z" fill="#e9ecf2"/>
      </svg>
    </div>
  </section>
</main>
</body>
</html>
```